'Cradle Ahead' promotional brochure

We have designed a 6 week program to educate impending first-time parents about the things they need to know to survive the first 6 months. Sessions delivered by general practitioner/family doctor, dietician, physiotherapist, speech pathologist and psychologist. Our promotional blurb is: 'A comprehensive education program for first-time parents-to-be, delivered over 6 weeks by health professionals in your community, about everything you need to know to look after your baby (and yourself!) in the first 6 months'. I now want to put together a promotional brochure to be distributed to those couples who express an interest which will provide further details of what will be delivered in the course.
Updates
In terms of layout, I envisaged a double sided A4 size, foldable into 3 sections, but very happy to be guided on this.
Target Market(s)
To appeal to a young, well educated demographic. First time parents couples.
Industry/Entity Type
Medical
Font styles to use
Other font styles liked:
- Playfair Display
Requirements
Must have
- Playfair display font to be consistent with our logo (attached). Logo also included please. Some consistency with colours of logo please.
Nice to have
- I am a doctor, and have no creative genes! But prefer a clean and professional appearance overall. Not too cluttered in overall appearance.
Should not have
- No cheesy pictures of babies.

```html
<!DOCTYPE html>
<html lang="en">
<head>
<meta charset="utf-8">
<title>Cradle Ahead – Brochure Inside Spread</title>
<link rel="stylesheet" href="https://fonts.googleapis.com/css2?family=Playfair+Display:wght@400;700&display=swap">
<style>
  :root {
    --green: #9dcb3c;
    --green-deep: #8cbf2c;
    --ink: #1f1f1f;
    --grey: #6f6f6f;
    --white: #ffffff;
    --black: #1b1b1b;
    --photo-light: #f3eeea;
    --photo-skin: #ecc9b4;
  }
  * { margin: 0; padding: 0; box-sizing: border-box; }
  html, body { width: 1200px; height: 848px; overflow: hidden; background: #fff; }
  body { font-family: "Playfair Display", Georgia, serif; color: var(--ink); }
  .spread { position: relative; width: 1200px; height: 848px; display: flex; }
  .panel { position: relative; height: 848px; }

  /* Left panel: week schedule */
  .panel--schedule { width: 392px; background: var(--white); }
  .edge-strip { position: absolute; left: 0; top: 228px; width: 26px; height: 620px; background: var(--green); border-top-right-radius: 22px; }
  .foot-bar { position: absolute; left: 26px; bottom: 0; width: 310px; height: 26px; background: var(--green); border-top-right-radius: 22px; }
  .week-pill { position: absolute; background: var(--green); color: var(--white); font-size: 33px; border-radius: 36px; padding: 0 22px; height: 50px; line-height: 48px; }
  .week-pill--5 { left: 26px; top: 22px; width: 154px; }
  .week-pill--6 { left: 40px; top: 348px; width: 150px; }
  .session { position: absolute; width: 345px; }
  .session h3 { font-size: 21px; font-weight: 700; margin-bottom: 8px; }
  .session p { font-size: 16.5px; line-height: 22.5px; }
  .session .highlight { color: var(--green); }
  .session--w5s1 { left: 38px; top: 88px; }
  .session--w6s1 { left: 49px; top: 412px; width: 332px; }
  .session--w6s2 { left: 49px; top: 630px; width: 332px; }

  /* Middle panel: hours & contact */
  .panel--contact { width: 406px; background: var(--green); color: var(--ink); }
  .brand-tab { position: absolute; left: 78px; top: 0; width: 250px; height: 174px; background: var(--white); border-radius: 0 0 14px 14px; display: flex; align-items: center; justify-content: center; gap: 10px; }
  .brand-mark { width: 14px; height: 14px; background: var(--green); }
  .brand-name { font-size: 19px; line-height: 24px; color: var(--grey); letter-spacing: 0.5px; }
  .clock { position: absolute; left: 174px; top: 230px; }
  .section-title { position: absolute; left: 0; width: 406px; text-align: center; font-size: 23px; letter-spacing: 0.5px; }
  .section-title--hours { top: 296px; }
  .hours { position: absolute; left: 18px; top: 328px; width: 362px; }
  .hours-row { display: flex; justify-content: space-between; font-size: 20.5px; line-height: 29px; }
  .hours-row b { font-weight: 700; }
  .section-title--contact { top: 471px; }
  .rule { position: absolute; left: 18px; top: 505px; width: 364px; height: 2px; background: var(--ink); }
  .address { position: absolute; left: 18px; top: 515px; display: flex; gap: 12px; font-size: 18.5px; line-height: 24.5px; }
  .phone { position: absolute; left: 70px; display: flex; align-items: center; gap: 12px; font-size: 30px; font-weight: 700; }
  .phone--voice { top: 606px; }
  .phone--fax { top: 651px; }
  .email { position: absolute; left: 32px; top: 716px; width: 360px; }
  .email-line { display: flex; align-items: center; gap: 6px; font-size: 14.5px; }
  .email-note { font-size: 9.5px; line-height: 11px; margin-left: 22px; }
  .web-band { position: absolute; left: 0; bottom: 0; width: 406px; height: 57px; background: var(--black); color: var(--white); font-size: 18.5px; line-height: 57px; padding-left: 18px; }

  /* Right panel: cover */
  .panel--cover { width: 402px; background: var(--white); }
  .cover-brand { position: absolute; left: 22px; top: 0; height: 180px; display: flex; align-items: center; gap: 14px; }
  .cover-brand .brand-mark { width: 20px; height: 20px; }
  .cover-brand .brand-name { font-size: 33px; line-height: 40px; }
  .cover-rule { position: absolute; left: 0; top: 180px; width: 402px; height: 6px; background: var(--green); }
  .cover-photo { position: absolute; left: 0; top: 186px; width: 402px; height: 662px; background: linear-gradient(180deg, #f4f1ee 0%, #efe6df 35%, var(--photo-skin) 62%, #f1ddd0 85%, #e9e4e0 100%); }
  .cover-title { position: absolute; left: 0; top: 186px; width: 402px; text-align: center; padding-top: 4px; }
  .cover-title h1 { font-size: 34px; font-weight: 400; margin-bottom: 8px; }
  .cover-title p { font-size: 14.5px; line-height: 21px; }
</style>
</head>
<body>
<main class="spread">

  <section class="panel panel--schedule">
    <div class="edge-strip"></div>
    <div class="foot-bar"></div>

    <div class="week-pill week-pill--5">Week 5</div>
    <article class="session session--w5s1">
      <h3>Session 1</h3>
      <p>Clinical Psychologist <span class="highlight">Dr Maren Ashby</span> will share information about bonding &amp; attachment with your baby, how to promote their social &amp; emotional development and how to manage separation anxiety. She will also discuss positive parenting approaches.</p>
    </article>

    <div class="week-pill week-pill--6">Week 6</div>
    <article class="session session--w6s1">
      <h3>Session 1</h3>
      <p>Secret Men’s Business – a men-only session (including beer!) with a new father for frank discussion about the road ahead. Mums will do a shopping excursion with the GP &amp; Dietician to Freshway to look at baby products and food – the good and the bad!</p>
    </article>
    <article class="session session--w6s2">
      <h3>Session 2</h3>
      <p>Program review, reflection and evaluation and future session planning when baby is 6 months of age.</p>
    </article>
  </section>

  <section class="panel panel--contact">
    <div class="brand-tab">
      <span class="brand-mark"></span>
      <span class="brand-name">BANKSIA<br>FAMILY HEALTH</span>
    </div>

    <svg class="clock" width="58" height="58" viewBox="0 0 58 58" aria-hidden="true">
      <circle cx="29" cy="29" r="26" fill="none" stroke="#fff" stroke-width="4"/>
      <circle cx="29" cy="29" r="19" fill="none" stroke="#fff" stroke-width="1.5"/>
      <path d="M29 16 V29 H38" fill="none" stroke="#fff" stroke-width="2.5" stroke-linecap="round"/>
    </svg>

    <h2 class="section-title section-title--hours">OPENING HOURS</h2>
    <div class="hours">
      <div class="hours-row"><span>Monday to Friday</span><b>8:30am – 5:00pm</b></div>
      <div class="hours-row"><span>Saturday</span><b>8:00am – 12:00pm</b></div>
      <div class="hours-row"><span>Sunday &amp; Public Holidays</span><b>Closed</b></div>
    </div>

    <h2 class="section-title section-title--contact">CONTACT INFORMATION</h2>
    <div class="rule"></div>
    <div class="address">
      <svg width="16" height="22" viewBox="0 0 16 22" aria-hidden="true"><path d="M8 0a8 8 0 0 0-8 8c0 6 8 14 8 14s8-8 8-14a8 8 0 0 0-8-8zm0 11a3 3 0 1 1 0-6 3 3 0 0 1 0 6z" fill="#fff"/></svg>
      <span>Wattle Grove Plaza, Shop 11<br>214 Wattle Grove Road<br>Wattle Grove NSW 2490</span>
    </div>

    <div class="phone phone--voice">
      <svg width="30" height="30" viewBox="0 0 24 24" aria-hidden="true"><path d="M6.6 10.8a15.1 15.1 0 0 0 6.6 6.6l2.2-2.2c.3-.3.7-.4 1-.2 1.1.4 2.3.6 3.6.6.6 0 1 .4 1 1V20c0 .6-.4 1-1 1C10.6 21 3 13.4 3 4c0-.6.4-1 1-1h3.5c.6 0 1 .4 1 1 0 1.3.2 2.5.6 3.6.1.3 0 .7-.2 1z" fill="#fff"/></svg>
      <span>02 5550 0188</span>
    </div>
    <div class="phone phone--fax">
      <svg width="30" height="30" viewBox="0 0 24 24" aria-hidden="true"><rect x="2" y="6" width="6" height="16" rx="1.5" fill="#fff"/><rect x="9" y="2" width="13" height="20" rx="1.5" fill="#fff"/><rect x="11" y="5" width="9" height="5" fill="#9dcb3c"/><g fill="#9dcb3c"><rect x="11" y="12" width="2" height="2"/><rect x="14.5" y="12" width="2" height="2"/><rect x="18" y="12" width="2" height="2"/><rect x="11" y="16" width="2" height="2"/><rect x="14.5" y="16" width="2" height="2"/><rect x="18" y="16" width="2" height="2"/></g></svg>
      <span>02 5550 0199</span>
    </div>

    <div class="email">
      <div class="email-line">
        <svg width="16" height="12" viewBox="0 0 16 12" aria-hidden="true"><rect width="16" height="12" fill="#fff"/><path d="M0 0 L8 7 L16 0" fill="none" stroke="#9dcb3c" stroke-width="1.2"/></svg>
        <span>reception@banksiafamilyhealth.com.au</span>
      </div>
      <p class="email-note">Please note this email service is checked once daily and is not available for making appointments or accessing medical advice.</p>
    </div>

    <div class="web-band">www.banksiafamilyhealth.com.au</div>
  </section>

  <section class="panel panel--cover">
    <div class="cover-brand">
      <span class="brand-mark"></span>
      <span class="brand-name">BANKSIA<br>FAMILY HEALTH</span>
    </div>
    <div class="cover-rule"></div>
    <div class="cover-photo" role="img" aria-label="Soft photograph of a parent's hands gently cradling a newborn's tiny feet"></div>
    <div class="cover-title">
      <h1>Cradle Ahead</h1>
      <p>A Comprehensive Education Program for<br>First-Time Parents<br>Delivered over 6 weeks by Health Professionals<br>in Your Community</p>
    </div>
  </section>

</main>
</body>
</html>
```